StageLoop - Music Industry App needs a top quality wordpress homepage

We need a modern responsive wordpress homepage built. Our website will only feature one page with the goal to get people to sign up to our app. A word document has been uploaded outlining the page content/sections.

Once the homepage is finalised, I will also need 2 landing pages built as part of this competition. It will be very similar to the homepage with the same layout etc but just feature different images and content. The homepage is for anyone (artists and venues) to find out about us but the landing pages will be artist or venue specific.

The completed work must be delivered as an exportable file into wordpress and be designed properly so no more work is needed to begin utilising as the actual website. The images used must be setup correctly for speed and quality also.

Target Market(s)

Venues and Artists.

Coding

Coded - Design and coding required

Requirements
Must have
• UPDATE: High Res Logo files attached
• Must be a modern looking website and be responsive. Must look good across all devices from desktop, to mobile and tablet. Needs to be very high quality.
• Please see the attached logo - I am waiting for the final high quality version and will reupload when complete but this will be enough to get you started for now. The website must have a dark base colour and have red/white elements to match the logo. The red colour used MUST match the red colour used in the logo.
• Please have a go at creating it how you think is best and provide feedback from there. I am leaving it very open to the designers so I can get the best website possible and lots of different ideas etc.

```html
<!DOCTYPE html>
<html lang="en">
<head>
<meta charset="utf-8">
<title>StageLoop – Zippa for live music</title>
<link rel="stylesheet" href="https://fonts.googleapis.com/css2?family=Montserrat:wght@400;500;600;700&family=Lato:ital,wght@0,400;0,700;1,400;1,700&display=swap">
<style>
:root{
  --red:#d0121b;
  --red-deep:#8e0b12;
  --red-dark:#5a070c;
  --black:#070707;
  --ink:#111;
  --white:#fff;
  --grey-text:#bdbdbd;
  --field:#f2f2f2;
  --field-line:#dcdcdc;
  --head:'Montserrat',sans-serif;
  --body:'Lato',sans-serif;
}
*{box-sizing:border-box;margin:0;padding:0}
html,body{width:1200px;height:4260px;overflow:hidden}
body{background:var(--black);font-family:var(--body);color:var(--white);position:relative}
.abs{position:absolute}
section,header,footer{position:absolute;left:0;width:1200px;overflow:hidden}

/* header / hero */
.hero{top:0;height:678px;background:radial-gradient(ellipse at 50% 10%,#e23a40 0%,#b3141b 35%,#5c0a0e 70%,#1c0204 100%)}
.hero-photo{position:absolute;inset:0;background:linear-gradient(180deg,rgba(0,0,0,0) 40%,rgba(0,0,0,.55) 85%,rgba(0,0,0,.75) 100%)}
.brand{position:absolute;display:flex;align-items:center;gap:10px;font-family:var(--head);font-weight:600;font-size:40px;color:var(--white);letter-spacing:-.5px}
.brand .dot{width:40px;height:40px;border-radius:50%;background:var(--white)}
.nav{position:absolute;top:44px;right:84px;display:flex;gap:37px;font-family:var(--head);font-size:14.5px;font-weight:500}
.hero-circle{position:absolute;left:393px;top:157px;width:414px;height:414px;border-radius:50%;background:rgba(206,18,26,.88)}
.hero h1{position:absolute;left:0;width:1200px;top:205px;text-align:center;font-family:var(--head);font-weight:700;font-size:58px;line-height:62px;text-transform:uppercase}
.hero .lead{position:absolute;left:0;width:1200px;top:340px;text-align:center;font-style:italic;font-size:18px;line-height:24px}
.hero .email{position:absolute;left:455px;top:408px;width:290px;height:48px;background:rgba(255,255,255,.22);font-size:14px;padding:16px 16px;color:#f4e4e4}
.btn-dark{position:absolute;background:#0c0c0c;color:var(--white);font-family:var(--head);font-size:14.5px;display:flex;align-items:center;justify-content:center;border-radius:3px}

/* how it works */
.how{top:678px;height:780px;background:linear-gradient(180deg,#050505,#000)}
.sec-title{position:absolute;left:0;width:1200px;text-align:center;font-family:var(--head);font-weight:600;font-size:40px}
.how .intro{position:absolute;left:0;width:1200px;top:150px;text-align:center;font-family:var(--head);font-size:16.5px;line-height:27px}
.eq-glow{position:absolute;top:120px;height:650px;width:280px;background:radial-gradient(ellipse at 50% 75%,rgba(150,14,22,.35) 0%,rgba(90,8,14,.18) 45%,transparent 75%)}
.step-num{position:absolute;width:72px;height:72px;border-radius:50%;background:#0a0a0a;border:2px solid #2a2a2a;box-shadow:0 0 0 4px #111;font-family:var(--head);font-size:34px;display:flex;align-items:center;justify-content:center}
.step-num.active{background:var(--red);border:3px solid var(--white)}
.step-text{position:absolute;font-family:var(--head);font-size:16.5px;line-height:27px;color:var(--grey-text)}
.phone-shot{position:absolute;left:509px;top:418px;width:180px;height:362px;border-radius:28px 28px 0 0;background:linear-gradient(180deg,#3a3f66 0%,#5b3c7a 40%,#2b2f4a 100%);border:4px solid #cfd2d8}

/* why */
.why{top:1458px;height:707px;background:linear-gradient(180deg,#121212 0%,#2a0a0c 45%,#8a0e15 100%)}
.tab{position:absolute;top:142px;font-family:var(--head);font-size:21px;transform:translateX(-50%)}
.track{position:absolute;left:355px;top:206px;width:486px;height:1px;background:#cfcfcf}
.node{position:absolute;top:196px;width:22px;height:22px;border-radius:50%;background:var(--white);border:5px solid #1a1a1a;box-shadow:0 0 0 2px var(--white)}
.node.on{background:var(--red)}
.card{position:absolute;border-radius:6px}
.feature-icon{position:absolute;left:692px;top:342px;width:136px;height:136px;border-radius:50%;background:var(--white);display:flex;align-items:center;justify-content:center}
.feature h3{position:absolute;left:694px;top:515px;font-family:var(--head);font-weight:500;font-size:31px}
.feature p{position:absolute;left:694px;top:562px;width:340px;font-family:var(--head);font-size:17px;line-height:30px}

/* venues / artists */
.venues{top:2165px;height:427px;background:linear-gradient(90deg,#2c0d20 0%,#6a1226 40%,#a3141c 100%)}
.artists{top:2592px;height:426px;background:linear-gradient(90deg,#6d0c12 0%,#8a1016 50%,#3a1a12 100%)}
.photo{position:absolute;top:0;height:100%}
.block h2{position:absolute;font-family:var(--head);font-weight:600;font-size:40px}
.block ul{position:absolute;list-style:none;font-size:14px;line-height:22px}
.block li{position:relative;padding-left:16px}
.block li::before{content:"";position:absolute;left:0;top:8px;width:6px;height:6px;border-radius:50%;background:var(--white)}
/* about */
.about{top:3018px;height:354px;background:linear-gradient(180deg,#5a0a0e,#7d0c12 60%,#9a0f16)}
.about .sub{position:absolute;left:0;width:1220px;top:140px;text-align:center;font-style:italic;font-size:20px}
.about p.body{position:absolute;left:198px;width:804px;top:180px;text-align:center;font-size:14px;font-weight:400;line-height:27.5px}
/* signup band */
.band{top:3372px;height:136px;background:#7c0910}
.band h4{position:absolute;left:79px;top:34px;font-family:var(--head);font-weight:500;font-size:26px;line-height:37px}
.band .field{position:absolute;left:550px;top:40px;width:572px;height:61px;background:var(--white);border-radius:3px}
.band .field span{position:absolute;left:44px;top:21px;font-style:italic;font-size:14px;color:#666}
/* contact */
.contact{top:3508px;height:674px;background:linear-gradient(180deg,#8d0d14 0%,#b0141b 50%,#4a0a0e 100%)}
.panel{position:absolute;left:159px;top:137px;width:886px;height:466px;background:rgba(120,80,80,.45)}
.white-card{position:absolute;top:167px;width:397px;height:406px;background:var(--white)}
.info{position:absolute;color:#333;font-size:14px;line-height:25px}
.info b{display:block;color:var(--red);font-family:var(--head);font-weight:500;font-size:17px;line-height:28px}
.input{position:absolute;left:643px;width:345px;background:var(--field);border:1px solid var(--field-line);color:#777;font-size:13.5px;padding:18px 11px}
footer{top:4182px;height:78px;background:#0c0c0c;text-align:center;font-size:12.5px;padding-top:30px}
</style>
</head>
<body>

<header class="hero">
  <div class="hero-photo" role="img" aria-label="Concert crowd with raised hands under red stage lights"></div>
  <div class="brand" style="left:78px;top:30px"><span class="dot"></span>StageLoop</div>
  <nav class="nav"><span>How StageLoop Works</span><span>Why StageLoop?</span><span>Venues</span><span>Artists</span><span>About</span><span>Contact</span></nav>
  <div class="hero-circle"></div>
  <h1>Zippa for live<br>music</h1>
  <p class="lead">StageLoop connects venues with artists to<br>make booking gigs simple</p>
  <div class="email">Enter Email</div>
  <div class="btn-dark" style="left:537px;top:469px;width:126px;height:52px">SIGN UP</div>
</header>

<section class="how" id="how">
  <div class="eq-glow" style="left:60px" role="img" aria-label="Faint red equalizer light pattern"></div>
  <div class="eq-glow" style="left:870px" role="img" aria-label="Faint red equalizer light pattern"></div>
  <h2 class="sec-title" style="top:48px">How StageLoop Works</h2>
  <p class="intro">Venues request a quote and<br>communicate with the artist direct</p>
  <svg class="abs" style="left:0;top:0" width="1200" height="780" aria-hidden="true">
    <circle cx="600" cy="504" r="235" fill="none" stroke="#2b2b2b" stroke-width="2"/>
    <circle cx="600" cy="504" r="157" fill="#9b9b9b"/>
  </svg>
  <div class="phone-shot" role="img" aria-label="Smartphone showing the music app playlist screen"></div>
  <div class="step-num active" style="left:562px;top:235px">3</div>
  <div class="step-num" style="left:356px;top:362px">2</div>
  <div class="step-num" style="left:769px;top:362px">4</div>
  <div class="step-num" style="left:349px;top:570px">1</div>
  <div class="step-num" style="left:776px;top:570px">5</div>
  <p class="step-text" style="left:130px;width:190px;top:356px;text-align:right">Venues search for an artist for theirup-coming gigs</p>
  <p class="step-text" style="left:108px;width:204px;top:564px;text-align:right">Artists and venues sign up for free and create a profile</p>
  <p class="step-text" style="left:876px;width:205px;top:356px">The gig is booked in once payment is provided by the venue.</p>
  <p class="step-text" style="left:884px;width:228px;top:564px">Upon completion the money is paid to the artist within 48 hours or less.</p>
</section>

<section class="why" id="why">
  <div class="abs" style="left:720px;top:100px;width:420px;height:420px;border-radius:50%;background:radial-gradient(circle,rgba(90,90,90,.35),transparent 70%)" role="img" aria-label="Studio microphone and mixing desk in low light"></div>
  <h2 class="sec-title" style="top:57px">Why StageLoop?</h2>
  <span class="tab" style="left:357px">Simple</span>
  <span class="tab" style="left:516px">Connect</span>
  <span class="tab" style="left:691px">Protection</span>
  <span class="tab" style="left:846px">Price</span>
  <div class="track"></div>
  <div class="node" style="left:344px"></div>
  <div class="node" style="left:506px"></div>
  <div class="node on" style="left:668px"></div>
  <div class="node" style="left:830px"></div>
  <div class="card" style="left:128px;top:281px;width:438px;height:291px;background:linear-gradient(135deg,#6b2c6a,#c07ab8)" role="img" aria-label="Music photo"></div>
  <div class="card" style="left:150px;top:302px;width:438px;height:291px;background:linear-gradient(135deg,#6a3a22,#b07a50)" role="img" aria-label="Music photo"></div>
  <div class="card" style="left:170px;top:323px;width:438px;height:291px;background:linear-gradient(135deg,#3c2a22,#8b6a52)" role="img" aria-label="Music photo"></div>
  <div class="card" style="left:190px;top:344px;width:438px;height:291px;background:linear-gradient(135deg,#1f6b70,#2d8a8e 50%,#164d52)" role="img" aria-label="Young woman dancing with headphones against a teal wall"></div>
  <div class="feature">
    <div class="feature-icon">
      <svg width="88" height="88" viewBox="0 0 88 88" fill="none" stroke="#111" stroke-width="3" aria-hidden="true">
        <path d="M20 40v-10a14 14 0 0 1 28 0v10"/>
        <rect x="12" y="40" width="44" height="36" rx="3"/>
        <circle cx="34" cy="56" r="5"/><path d="M34 61v8"/>
        <path d="M62 14l16 6v14c0 10-7 17-16 20-9-3-16-10-16-20V20z" fill="#fff"/>
        <path d="M55 33l5 5 10-10"/>
      </svg>
    </div>
    <h3>Protection</h3>
    <p>Everyone is protected with our complimentary dispute resolutions.</p>
  </div>
</section>

<section class="venues block" id="venues">
  <div class="photo" style="left:0;width:560px;background:radial-gradient(ellipse at 30% 50%,#b0603c 0%,#5a2030 45%,transparent 80%)" role="img" aria-label="Guitarist playing an electric guitar on a dim stage"></div>
  <h2 style="left:605px;top:60px">Venues</h2>
  <p class="abs" style="left:605px;top:133px;width:510px;font-style:italic;font-weight:700;font-size:13.5px;line-height:25.5px">StageLoop is not yet ready to host gigs as we're currently working on building our artists. We are launching for venues in Q4 2019. Pre-register now to keep informed and be one of the first people to use our platform.</p>
  <ul style="left:605px;top:216px;line-height:31.5px">
    <li>StageLoop is a 100% FREE service for all venues - you pay us nothing!</li>
    <li>Get instant access to hundreds of artists around your local community</li>
    <li>All genres to suit any venue from a pub to a wedding or even a nightclub</li>
    <li>Simple booking process with a money back guarantee</li>
    <li>Communicate directly with the artist and negotiate the price</li>
  </ul>
</section>

<section class="artists block" id="artists">
  <div class="photo" style="left:562px;width:638px;background:linear-gradient(90deg,rgba(0,0,0,0),#6b4a38 30%,#a27a5e 60%,#3a2a22)" role="img" aria-label="Smiling couple sitting together at a piano"></div>
  <h2 style="left:79px;top:60px">Artists</h2>
  <ul style="left:79px;top:132px;width:450px">
    <li style="margin-bottom:14px">Sign up to StageLoop for FREE and get yourself in front of venues</li>
    <li style="margin-bottom:14px">Only pay us if you get a gig - we only get 5% of the fee you charge \the venue</li>
    <li style="margin-bottom:14px">All genres and artists welcome - as long as you're experienced and professional</li>
    <li style="margin-bottom:14px">Get paid within 48 hours or less after the gig guaranteed!</li>
    <li>Negotiate your price and don't pay huge agent fees to ensure you earn top dollar</li>
  </ul>
</section>

<section class="about" id="about">
  <h2 class="sec-title" style="top:60px">About StageLoop</h2>
  <p class="sub">General Blurb about StageLoop an the founders</p>
  <p class="body">Lorem ipsum dolor sit amet, consectetur adipiscing elit, sed deiusmod tempor incididunt ut labore et dolore magna aliqua. Ut enim ad minim veniam, quis nostrud exercitation ullamco laboris nisi ut aliquip ex ea commodo consequat. Duis aute irure dolor in reprehenderit in voluptate velit esse cillum dolore eu fugiat nulla pariatur. Excepteur sint occaecat cupidatat non proident, sunt in culpa qui officia deserunt mollit anim id est laborum.</p>
</section>

<section class="band">
  <h4>Sign up and create your StageLoop<br>profile now</h4>
  <div class="field">
    <svg class="abs" style="left:10px;top:22px" width="22" height="16" viewBox="0 0 22 16" aria-hidden="true"><rect x="1" y="1" width="20" height="14" fill="none" stroke="#d0121b" stroke-width="2"/><path d="M1 1l10 8 10-8M1 15l7-7M21 15l-7-7" fill="none" stroke="#d0121b" stroke-width="2"/></svg>
    <span>Enter Email here....</span>
    <div class="btn-dark" style="left:443px;top:5px;width:126px;height:51px;border-radius:3px">REGISTER</div>
  </div>
</section>

<section class="contact" id="contact">
  <h2 class="sec-title" style="top:60px">Contact us</h2>
  <div class="panel"></div>
  <div class="white-card" style="left:190px"></div>
  <div class="white-card" style="left:618px"></div>
  <div class="brand" style="left:213px;top:198px;color:#1a1a1a;font-size:40px"><span class="dot" style="background:var(--red)"></span>StageLoop</div>
  <svg class="abs" style="left:212px;top:294px" width="18" height="22" viewBox="0 0 18 22" aria-hidden="true"><path d="M9 1a7 7 0 0 0-7 7c0 5 7 13 7 13s7-8 7-13a7 7 0 0 0-7-7z" fill="#d0121b"/><circle cx="9" cy="8" r="2.6" fill="#fff"/></svg>
  <div class="info" style="left:251px;top:286px"><b>StageLoop</b>123, Address, State Name,<br>City Name,Zipcode</div>
  <svg class="abs" style="left:212px;top:396px" width="22" height="22" viewBox="0 0 24 24" aria-hidden="true"><path d="M6.6 10.8a15 15 0 0 0 6.6 6.6l2.2-2.2a1 1 0 0 1 1-.25 11.4 11.4 0 0 0 3.6.6 1 1 0 0 1 1 1V20a1 1 0 0 1-1 1A17 17 0 0 1 3 4a1 1 0 0 1 1-1h3.5a1 1 0 0 1 1 1 11.4 11.4 0 0 0 .6 3.6 1 1 0 0 1-.25 1z" fill="#d0121b"/></svg>
  <div class="info" style="left:251px;top:392px"><b>Telephone</b>123-456-7890</div>
  <svg class="abs" style="left:212px;top:474px" width="22" height="16" viewBox="0 0 22 16" aria-hidden="true"><rect x="1" y="1" width="20" height="14" fill="none" stroke="#d0121b" stroke-width="2"/><path d="M1 1l10 8 10-8M1 15l7-7M21 15l-7-7" fill="none" stroke="#d0121b" stroke-width="2"/></svg>
  <div class="info" style="left:251px;top:464px"><b>Email Address</b>info@stageloop.com</div>
  <div class="input" style="top:188px;height:56px">Name* :</div>
  <div class="input" style="top:256px;height:56px">Email* :</div>
  <div class="input" style="top:324px;height:56px">Phone* :</div>
  <div class="input" style="top:391px;height:93px">Message / comments :</div>
  <div class="btn-dark" style="left:643px;top:496px;width:126px;height:49px">SUBMIT</div>
</section>

<footer>Copyright © <b>StageLoop</b> - 2019 . All Right Reserved</footer>

</body>
</html>
```